Bright Path Therapies business cards and stationary

Need business cards and stationary designed to match previously made logo for for a new company based in Sydney NSW called 'Bright Path Therapies'.

We provide early intervention services and diagnostic assessment for children with disability and their families. I would like designs that are colourful and child friendly - possibly using feet/footprints/steps on a white background. The final design should communicate that we are family friendly, accepting and fun to work with.

Target Market(s)

Parents and Families
Teachers
Allied Health Professionals

Industry/Entity Type

Psychology

Contact Information for Business Card

Bright Path Therapies
www.brightpaththerapies.example
info@brightpaththerapies.example

Font styles to use
Sans Serif
Decorative
Script

Requirements
Must have
• Match the font and colour scheme of logo, along with footprint picture
Nice to have
• Clean and simple, while reflecting that I am working with families.
• Also- editable for when we make staff specific cards.

```html
<!DOCTYPE html>
<html lang="en">
<head>
<meta charset="utf-8">
<title>Bright Path Therapies – Business Cards</title>
<link rel="stylesheet" href="https://fonts.googleapis.com/css2?family=Questrial&display=swap">
<style>
  :root {
    --backdrop: #e7e5e2;
    --paper: #ffffff;
    --orange: #f39120;
    --red: #ee3424;
    --red-deep: #d52427;
    --peach: #f4c3b0;
    --ink: #2a2a2a;
    --text-font: "Questrial", sans-serif;
  }
  * { box-sizing: border-box; margin: 0; padding: 0; }
  html, body {
    width: 1200px; height: 997px; overflow: hidden;
    background: var(--backdrop);
    font-family: var(--text-font);
  }
  .card {
    position: absolute; left: 250px;
    width: 700px; height: 400px;
    overflow: hidden;
    box-shadow: 0 6px 18px rgba(0,0,0,0.12);
  }
  .card--front { top: 68px; background: var(--paper); }
  .card--back { top: 528px; background: var(--red); }

  .card__shapes { position: absolute; inset: 0; }

  .contact {
    position: absolute; left: 400px; top: 82px;
    list-style: none; color: var(--ink); font-size: 17px;
  }
  .contact__item { display: flex; align-items: center; gap: 9px; margin-bottom: 10px; }
  .contact__icon {
    width: 18px; height: 18px; border-radius: 50%;
    background: var(--red); display: flex; align-items: center; justify-content: center;
  }

  .brand { position: absolute; display: flex; align-items: center; gap: 14px; }
  .brand__dot { border-radius: 50%; flex: none; }
  .brand__name { font-weight: 400; white-space: nowrap; letter-spacing: 1px; }

  .card--front .brand { left: 38px; top: 204px; }
  .card--front .brand__dot { width: 56px; height: 56px; background: var(--red); }
  .card--front .brand__name { font-size: 27px; color: var(--red); }

  .card--back .brand { right: 40px; top: 168px; }
  .card--back .brand__dot { width: 60px; height: 60px; background: var(--paper); }
  .card--back .brand__name { font-size: 30px; color: var(--paper); }
</style>
</head>
<body>

<section class="card card--front" aria-label="Business card front">
  <svg class="card__shapes" width="700" height="400" viewBox="0 0 700 400">
    <path class="orange-panel" fill="var(--orange)"
      d="M215,0 H700 V400 H395 V190 Q395,165 370,165 H240 Q215,165 215,140 Z"/>
    <g role="img" aria-label="Soft peach footprint trail walking up from the lower left">
      <ellipse cx="250" cy="365" rx="150" ry="70" fill="var(--peach)" opacity="0.55"/>
      <ellipse cx="330" cy="300" rx="70" ry="45" fill="var(--peach)" opacity="0.55"/>
    </g>
  </svg>

  <ul class="contact">
    <li class="contact__item">
      <span class="contact__icon">
        <svg width="10" height="8" viewBox="0 0 10 8"><rect x="0.5" y="0.5" width="9" height="7" fill="none" stroke="#fff"/><path d="M0.5,0.5 L5,4.5 L9.5,0.5" fill="none" stroke="#fff"/></svg>
      </span>
      <span class="contact__text">www.brightpaththerapies.example</span>
    </li>
    <li class="contact__item">
      <span class="contact__icon">
        <svg width="10" height="10" viewBox="0 0 10 10"><circle cx="5" cy="5" r="4" fill="none" stroke="#fff"/><circle cx="5" cy="5" r="1.5" fill="#fff"/></svg>
      </span>
      <span class="contact__text">info@brightpaththerapies.example</span>
    </li>
  </ul>

  <div class="brand">
    <span class="brand__dot"></span>
    <span class="brand__name">Bright Path Therapies</span>
  </div>
</section>

<section class="card card--back" aria-label="Business card back">
  <svg class="card__shapes" width="700" height="400" viewBox="0 0 700 400">
    <g role="img" aria-label="Deep red footprint trail stepping across the left side">
      <ellipse cx="150" cy="250" rx="170" ry="150" fill="var(--red-deep)" opacity="0.6"/>
      <ellipse cx="260" cy="130" rx="90" ry="80" fill="var(--red-deep)" opacity="0.5"/>
    </g>
  </svg>

  <div class="brand">
    <span class="brand__dot"></span>
    <span class="brand__name">Bright Path Therapies</span>
  </div>
</section>

</body>
</html>
```